Brennock Metal recycling, a business card/logo for our industrial family metal recycling company

A new business card design/logo for our long established family metal recycling company.
I have a logo for our property company which was designed a few months ago on pixel forum which I would like to be very close to this design but have a more industrial feel to it and in a darker blue colour, please see attachments.

Target Market(s)

industries that produce metal waste for recycling, construction sites, engineering companies, manufactures, builders, plumbers, electricians, general house holders.

Industry/Entity Type

Recycling

Contact Information for Business Card

owner/director...Gordon brennock
e-mail....info@brennockscrapworks.example.co.uk
web address.....brennockscrapworks.example.co.uk

Font styles to use
Serif
Sans Serif

Colors
0255a3
ffffff

Requirements
Must have
• -dark blue business card on front.
-white on the back, see contact details, e-mail address for metal company.
-to have an industrial feel to it.
-brennock logo as business card attached but (brennock metal recycling)
please remove the little roof/arrow above brennock as this was relevant to property company.
Nice to have
• please see our website brennockscrapworks.example.co.uk with all details
being correct however I would like to refresh the logo to more like the brennock property investment business card logo attached.
Should not have
• should not contain details from property investments card as this design is for the metal recycling company.

```html
<!DOCTYPE html>
<html lang="en">
<head>
<meta charset="utf-8">
<title>Brennock Metal Recycling – Business Card</title>
<link rel="stylesheet" href="https://fonts.googleapis.com/css2?family=Arimo:wght@400;700&display=swap">
<style>
  :root {
    --brand-blue: #0255a3;
    --card-white: #ffffff;
    --paper: #f3f3f1;
    --ink: #1c1c1c;
    --ink-soft: #3a3a3a;
    --backdrop: #4a4b4e;
  }
  * { box-sizing: border-box; margin: 0; padding: 0; }
  html, body {
    width: 1200px; height: 1000px; overflow: hidden;
    background: var(--backdrop);
    font-family: "Arimo", Arial, sans-serif;
  }
  .canvas { position: relative; width: 1200px; height: 1000px; }

  .card {
    position: absolute;
    width: 620px; height: 360px;
    border-radius: 34px;
  }

  /* Front */
  .card--front {
    left: 90px; top: 90px;
    background: var(--paper);
    padding: 14px;
  }
  .front-panel {
    position: relative;
    width: 100%; height: 100%;
    background: var(--brand-blue);
    border-radius: 22px;
    overflow: hidden;
  }
  .front-logo {
    position: absolute; left: 0; right: 0; top: 80px;
    display: flex; flex-direction: column; align-items: center;
  }
  .logo-lockup { display: flex; align-items: center; gap: 16px; }
  .logo-dot {
    width: 26px; height: 26px; border-radius: 50%;
    background: var(--card-white);
  }
  .logo-name { font-weight: 400; letter-spacing: 3px; line-height: 1; }
  .front-logo .logo-name { font-size: 84px; color: var(--card-white); }
  .logo-tagline {
    font-weight: 400; text-transform: uppercase; letter-spacing: 6px;
    line-height: 1; white-space: nowrap;
  }
  .front-logo .logo-tagline {
    margin-top: 10px; margin-left: 42px;
    font-size: 17px; color: var(--card-white);
  }
  .service-strip {
    position: absolute; left: 0; right: 0; bottom: 30px;
    height: 40px; background: var(--paper);
    display: flex; align-items: center; justify-content: center;
    color: var(--brand-blue);
    font-weight: 700; font-size: 24px; letter-spacing: 0.5px;
    white-space: nowrap;
  }

  /* Back */
  .card--back {
    left: 490px; top: 560px;
    background: var(--brand-blue);
    padding: 18px;
  }
  .back-panel {
    position: relative;
    width: 100%; height: 100%;
    background: var(--paper);
    border-radius: 18px;
  }
  .back-logo {
    position: absolute; left: 30px; top: 36px;
    display: flex; flex-direction: column; align-items: flex-start;
  }
  .back-logo .logo-lockup { gap: 12px; }
  .back-logo .logo-dot { width: 18px; height: 18px; background: var(--brand-blue); }
  .back-logo .logo-name { font-size: 58px; color: var(--brand-blue); }
  .back-logo .logo-tagline {
    margin-top: 6px; margin-left: 34px;
    font-size: 12px; letter-spacing: 4px; color: var(--ink-soft);
  }
  .company-address {
    position: absolute; right: 26px; top: 40px;
    text-align: right; font-style: normal;
    font-weight: 700; font-size: 13px; line-height: 1.55;
    color: var(--ink-soft);
  }
  .person { position: absolute; left: 34px; top: 140px; }
  .person-name {
    font-weight: 700; font-size: 26px; color: var(--brand-blue);
    letter-spacing: 1px; text-transform: uppercase;
  }
  .person-role { font-weight: 700; font-size: 22px; color: var(--ink); margin-top: 2px; }
  .contact-list {
    position: absolute; left: 34px; bottom: 26px;
    list-style: none; font-weight: 700; font-size: 14px; color: var(--ink);
  }
  .contact-list li { display: flex; align-items: center; gap: 10px; margin-top: 8px; }
  .contact-icon { width: 20px; height: 20px; flex: none; }
  .contact-list .accent { color: var(--brand-blue); }
</style>
</head>
<body>
<main class="canvas">

  <section class="card card--front" aria-label="Business card front">
    <div class="front-panel">
      <div class="front-logo">
        <div class="logo-lockup">
          <span class="logo-dot" aria-hidden="true"></span>
          <span class="logo-name">brennock</span>
        </div>
        <span class="logo-tagline">Metal Recycling</span>
      </div>
      <div class="service-strip">SCRAP • METALS • COLLECTION • RECYCLING</div>
    </div>
  </section>

  <section class="card card--back" aria-label="Business card back">
    <div class="back-panel">
      <div class="back-logo">
        <div class="logo-lockup">
          <span class="logo-dot" aria-hidden="true"></span>
          <span class="logo-name">brennock</span>
        </div>
        <span class="logo-tagline">Metal Recycling</span>
      </div>

      <address class="company-address">
        D Brennock Metals Ltd,<br>
        Unit 4,12B Halden Road,<br>
        London SE99 1ZZ
      </address>

      <div class="person">
        <p class="person-name">Gordon Brennock</p>
        <p class="person-role">owner/director</p>
      </div>

      <ul class="contact-list">
        <li>
          <svg class="contact-icon" viewBox="0 0 20 20" aria-hidden="true">
            <circle cx="10" cy="10" r="10" fill="var(--brand-blue)"/>
            <path d="M6.5 5.5c.6-.6 1.3-.5 1.7.1l.9 1.4c.3.5.2 1-.2 1.4l-.6.5c.6 1.3 1.5 2.2 2.8 2.8l.5-.6c.4-.4.9-.5 1.4-.2l1.4.9c.6.4.7 1.1.1 1.7l-.7.7c-.6.6-1.6.7-2.5.3-2.4-1.1-4.2-2.9-5.3-5.3-.4-.9-.3-1.9.3-2.5z" fill="#fff"/>
          </svg>
          <span>079 000 46 135 // 020 000 58 274</span>
        </li>
        <li>
          <svg class="contact-icon" viewBox="0 0 20 20" aria-hidden="true">
            <circle cx="10" cy="10" r="10" fill="var(--brand-blue)"/>
            <rect x="5" y="6.5" width="10" height="7" rx="1" fill="#fff"/>
            <path d="M5.4 7l4.6 3.6L14.6 7" fill="none" stroke="var(--brand-blue)" stroke-width="1"/>
          </svg>
          <span>info<span class="accent">@brennockscrapworks.example</span>.co.uk</span>
        </li>
        <li>
          <svg class="contact-icon" viewBox="0 0 20 20" aria-hidden="true">
            <circle cx="10" cy="10" r="10" fill="var(--brand-blue)"/>
            <circle cx="10" cy="10" r="5" fill="none" stroke="#fff" stroke-width="1.2"/>
            <ellipse cx="10" cy="10" rx="2.2" ry="5" fill="none" stroke="#fff" stroke-width="1"/>
            <line x1="5" y1="10" x2="15" y2="10" stroke="#fff" stroke-width="1"/>
          </svg>
          <span>www.<span class="accent">brennockscrapworks.example</span>.co.uk</span>
        </li>
      </ul>
    </div>
  </section>

</main>
</body>
</html>
```